" O escritório Brunoro Arquitetura desenvolve projetosarquitetônicos e interiores, além de acompanhamento e administraçãao de obras. Tem a frente de sua gestão a arquiteta Mariana Forteso, que prioriza o atendimento exclusivo e diferenciado a cada um dos clientes, estabelecendo assim uma relação de proximidade, confiança e fidelização. Todos os projetos são desenvolvidos de acordo com o perfil do cliente, buscando sempre soluções inovadoras, criativas e acessíveis, em muitos casos utilizando materiais e soluções alternativas ao convencional, marca do escritório. O espaço físico do escritório reflete essa proposta de inovação e criatividade, que permite a acessibilidade da arquitetura a qualquer pessoa, desmistificando o status de que a boa arquitetura é acessível somente àqueles que possuem um alto poder aquisitivo. Todo o processo de concepção e posterior execução dos trabalhos é realizada entre os profissionais envolvidos e os clientes com total transparência, sendo a política de trabalho do escritório focada na ética, honestidade e respeito ao cliente, não havendo portanto o recebimento de reservas técnicas ou comissões de lojistas e empresas terceiras, para indicação de produtos. Assim, trabalhamos com total liberdade na concepção e especificação de materiais e soluções nos projetos. O escritório também tem ligação forte com as escolas de arquitetura da cidade, sendo um local de estágio e constante aprendizado para estudantes, que adquirem experiência profissional junto aos membros do escritório. A linguagem dos projetos, que deve se refletir na identidade visual da marca, busca a simplicidade dos materiais e formas, aplicadas da forma correta, gerando resultados simples, porém sofisticados. Priorizamos o uso dos materiais naturais em todos os projetos, mas prioritariamente o uso da madeira natural. Trabalhamos sempre com muito respeito pela história dos lugares, procurando sempre que possível preservar características originais que dão identidade aos lugares. "

```html
<!DOCTYPE html>
<html lang="pt-BR">
<head>
<meta charset="utf-8">
<title>Brunoro Arquitetura – Assinatura de Email</title>
<link rel="stylesheet" href="https://fonts.googleapis.com/css2?family=Oswald:wght@500&family=Roboto:wght@300;400&display=swap">
<style>
  :root {
    --bg-center: #f6f6f6;
    --bg-edge: #9c9c9c;
    --tab-dark: #5f6265;
    --tab-light: #d4d4d4;
    --band-dark: #6d7073;
    --band-light: #c9cbcd;
    --card: #ffffff;
    --decor: #f1f1f2;
    --text: #5a5d60;
    --text-soft: #9a9c9e;
    --white: #ffffff;
  }
  * { margin: 0; padding: 0; box-sizing: border-box; }
  html, body { width: 1200px; height: 1200px; overflow: hidden; }
  body {
    position: relative;
    background: radial-gradient(ellipse 75% 70% at 50% 52%, var(--bg-center) 0%, #dcdcdc 45%, var(--bg-edge) 100%);
    font-family: "Roboto", Arial, sans-serif;
    color: var(--text);
  }
  .section-tab { position: absolute; left: 0; top: 26px; width: 440px; height: 56px; }
  .section-tab svg { position: absolute; left: 0; top: 0; }
  .section-tab__label {
    position: absolute; left: 150px; top: 11px;
    font-family: "Oswald", "Arial Narrow", sans-serif; font-weight: 500;
    font-size: 24px; color: var(--white);
    text-transform: uppercase; line-height: 32px;
  }
  .signature { position: absolute; left: 91px; top: 447px; width: 1018px; height: 306px; }
  .signature__band { position: absolute; left: 0; top: 0; width: 100%; height: 19px; background: var(--band-dark); }
  .signature__rule { position: absolute; left: 0; top: 19px; width: 100%; height: 5px; background: var(--band-light); }
  .signature__card {
    position: absolute; left: 0; top: 24px; width: 100%; height: 282px;
    background: var(--card); box-shadow: 0 2px 6px rgba(0,0,0,0.08); overflow: hidden;
  }
  .signature__decor {
    position: absolute; left: 55px; top: 0; width: 720px; height: 282px;
    background: linear-gradient(90deg, rgba(241,241,242,0) 0%, var(--decor) 25%, var(--decor) 75%, rgba(241,241,242,0) 100%);
  }
  .brand { position: absolute; left: 58px; top: 62px; width: 320px; }
  .brand__mark {
    display: block; width: 70px; height: 70px; margin: 0 0 22px 0;
    border: 3px solid var(--text); border-radius: 50%;
  }
  .brand__name {
    font-weight: 300; font-size: 29px; line-height: 36px; color: var(--text);
  }
  .brand__web { font-size: 19px; line-height: 24px; margin-top: 22px; color: var(--text); }
  .contact {
    position: absolute; right: 56px; top: 30px; text-align: right;
    font-size: 21px; line-height: 26.5px; color: var(--text);
  }
  .contact__name { font-size: 26px; line-height: 30px; color: var(--text-soft); font-weight: 300; }
  .contact__address { margin-top: 14px; }
  .contact__phones { margin-top: 14px; }
  .contact__label { color: var(--text-soft); font-weight: 300; }
  .contact__mail { margin-top: 8px; }
</style>
</head>
<body>
  <div class="section-tab">
    <svg width="440" height="56" viewBox="0 0 440 56" aria-hidden="true">
      <polygon points="0,0 440,0 440,22 418,22 418,56 0,56" fill="var(--tab-light)"/>
      <polygon points="80,6 420,6 404,50 80,50" fill="var(--tab-dark)"/>
      <polygon points="412,6 430,6 430,22" fill="var(--tab-dark)"/>
    </svg>
    <div class="section-tab__label">Assinatura de Email</div>
  </div>

  <section class="signature">
    <div class="signature__band"></div>
    <div class="signature__rule"></div>
    <div class="signature__card">
      <div class="signature__decor" role="img" aria-label="Faint large decorative brand motif in the card background"></div>
      <div class="brand">
        <span class="brand__mark"></span>
        <div class="brand__name">Brunoro Arquitetura</div>
        <div class="brand__web">www.brunoroarq.com.br</div>
      </div>
      <div class="contact">
        <div class="contact__name">Mariana Forteso</div>
        <div class="contact__cau">CAU - 48213-07</div>
        <div class="contact__address">
          Rua Jardim Aurora, 845<br>
          Bairro: Vila Nova | CEP: 04512-330<br>
          Campinas/SP
        </div>
        <div class="contact__phones"><span class="contact__label">Telefones:</span> (19) 3344-5566 | (19) 9876-5432</div>
        <div class="contact__mail">contato@brunoroarq.com.br</div>
      </div>
    </div>
  </section>
</body>
</html>
```